Building/Renovation Company needs Website

I need a website designed for a renovation/building company based in Hampshire. We specialise in kitchens, bathrooms, carpentry, plastering, brickwork, ground/garden works and decorating, and all our work is fully insured and carried out to a high standard.

With the photos, display them in a before/after format.

Coding

Coded - Design and coding required

Number of Pages Required

1 page

```html
<!DOCTYPE html>
<html lang="en">
<head>
<meta charset="utf-8">
<title>Harwell Builds – Property Renovation &amp; Building Services</title>
<link href="https://fonts.googleapis.com/css2?family=Montserrat:ital,wght@0,400;0,500;0,600;0,700;0,800;1,400&family=Oswald:wght@600&display=swap" rel="stylesheet">
<style>
:root{
  --blue:#232e8c;
  --lime:#d3dc1d;
  --ink:#333;
  --grey:#f2f2f2;
  --white:#fff;
}
*{box-sizing:border-box;margin:0;padding:0}
html,body{width:1200px;height:4431px;overflow:hidden}
body{position:relative;font-family:"Montserrat",sans-serif;color:var(--ink);background:var(--white)}
.abs{position:absolute}
.brand{font-family:"Montserrat",sans-serif;font-weight:600;color:var(--blue);font-size:28px;display:flex;align-items:center;gap:10px}
.brand .mark{width:26px;height:26px;background:var(--lime)}
.topbar{left:690px;top:0;width:510px;height:52px;background:var(--blue);clip-path:polygon(4% 0,100% 0,100% 100%,0 100%);color:var(--white);font-size:14px;font-weight:500;display:flex;align-items:center;gap:30px;padding-left:30px}
.topbar span{display:flex;align-items:center;gap:8px}
.nav{top:76px;left:406px;display:flex;gap:39px;font-size:14px;font-weight:600;color:#222}
.nav .active{color:var(--blue);border-bottom:3px solid var(--lime);padding-bottom:8px}
.hero{left:0;top:120px;width:1200px;height:610px;background:linear-gradient(180deg,#bdbdbd 0%,#d8d3cb 45%,#b38a5a 80%,#9b6f42 100%)}
.hero-title{left:0;top:290px;width:1200px;text-align:center;font-family:"Oswald",sans-serif;font-weight:600;font-size:72px;line-height:80px;color:var(--white);text-transform:uppercase}
.photo{background:linear-gradient(160deg,#c9c9c9,#7b7b7b)}
.h2{font-weight:800;color:var(--blue);text-transform:uppercase}
.about-title{left:575px;top:830px;font-size:46px}
.about-sub{left:575px;top:902px;width:520px;font-size:24px;line-height:26px;font-weight:700;color:var(--lime)}
.about-text{left:575px;top:998px;width:500px;font-size:15px;line-height:24px;color:#444}
.btn{background:var(--lime);color:var(--blue);font-weight:700;font-size:15px;text-transform:uppercase;display:flex;align-items:center;justify-content:center}
.services{left:0;top:1408px;width:1200px;height:610px;background:var(--blue)}
.services-title{left:0;top:1470px;width:1200px;text-align:center;color:var(--white);font-size:42px}
.svc{width:200px;text-align:center;color:var(--white);font-weight:600;font-size:20px;line-height:24px}
.svc svg{display:block;margin:0 auto 12px}
.projects-title{left:0;top:2102px;width:1200px;text-align:center;font-size:42px}
.card{background:var(--grey)}
.tag{background:var(--lime);color:var(--blue);font-weight:700;font-size:16px;width:110px;height:38px;display:flex;align-items:center;justify-content:center}
.why{left:0;top:2835px;width:1200px;height:525px;background:var(--lime)}
.why-title{left:685px;top:2960px;font-size:40px}
.why-list{left:700px;top:3027px;list-style:none;color:var(--blue);font-weight:600;font-size:21px}
.why-list li{display:flex;align-items:center;gap:12px;height:43.5px}
.testi-title{left:0;top:3465px;width:1200px;text-align:center;font-size:40px;font-weight:700}
.testi-box{left:228px;top:3548px;width:745px;height:247px;border:2px solid var(--lime)}
.testi-text{left:280px;top:3590px;width:640px;text-align:center;font-style:italic;font-size:18px;line-height:30px;color:#444}
.testi-name{left:0;top:3728px;width:1200px;text-align:center;color:var(--blue);font-weight:700;font-size:20px}
.quote{left:248px;top:3690px;font-size:110px;font-weight:800;color:var(--lime);line-height:1}
.estimate{left:0;top:3925px;width:1200px;height:143px;background:var(--blue)}
.estimate-text{left:327px;top:3974px;color:var(--white);font-weight:700;font-size:34px;text-transform:uppercase}
.foot-h{font-weight:600;font-size:20px;color:#111}
.foot-list{list-style:none;font-size:15px;line-height:24px;color:#555}
.contact-row{display:flex;align-items:flex-start;gap:10px;font-size:15px;color:#555;line-height:19px}
.ico{width:26px;height:26px;border-radius:50%;background:var(--blue);flex:none;display:flex;align-items:center;justify-content:center}
.rule{left:0;top:4345px;width:1200px;height:2px;background:#222}
.copy{left:0;top:4376px;width:1200px;text-align:center;font-size:14px;color:#555}
</style>
</head>
<body>

<header>
  <div class="abs brand" style="left:78px;top:40px"><span class="mark"></span>Harwell Builds</div>
  <div class="abs topbar">
    <span><svg width="14" height="14" viewBox="0 0 24 24"><path fill="#d3dc1d" d="M6.6 10.8a15 15 0 0 0 6.6 6.6l2.2-2.2c.3-.3.7-.4 1-.2 1.1.4 2.3.6 3.6.6.6 0 1 .4 1 1V20c0 .6-.4 1-1 1A17 17 0 0 1 3 4c0-.6.4-1 1-1h3.5c.6 0 1 .4 1 1 0 1.3.2 2.5.6 3.6.1.3 0 .7-.2 1z"/></svg>0790 000 1234</span>
    <span><svg width="14" height="12" viewBox="0 0 24 18"><rect width="24" height="18" rx="2" fill="#d3dc1d"/><path d="M2 2l10 8 10-8" stroke="#232e8c" stroke-width="2" fill="none"/></svg>hello@harwellbuilds.co.uk</span>
  </div>
  <nav class="abs nav">
    <span class="active">HOME</span><span>ABOUT US</span><span>SERVICES</span><span>WHY CHOOSE US?</span><span>GALLERY</span><span>CONTACT</span>
  </nav>
</header>

<section>
  <div class="abs hero" role="img" aria-label="Bright renovated open-plan kitchen with grey cabinets and wooden floor"></div>
  <svg class="abs" style="left:0;top:630px" width="1200" height="110" viewBox="0 0 1200 110">
    <polygon points="0,95 1200,0 1200,110 0,110" fill="#fff"/>
    <polygon points="420,95 1200,10 1200,78" fill="#d3dc1d"/>
  </svg>
  <h1 class="abs hero-title">Property Renovation<br>&amp; Building Services</h1>
</section>

<section>
  <div class="abs photo" style="left:128px;top:830px;width:403px;height:456px;background:linear-gradient(180deg,#d9d9d9,#2c3440 55%,#1f2730)" role="img" aria-label="Renovated kitchen with dark cabinets and window above the sink"></div>
  <h2 class="abs h2 about-title">About Us</h2>
  <p class="abs about-sub">Delivering High-Quality workmanship across Hamphire and surrounding counties.</p>
  <p class="abs about-text">Lorem ipsum dolor sit amet, consectetur adipiscing elit, sed do eiusmod tempor incididunt ut labore et dolore magna aliqua. Quis ipsum suspendisse ultrices gravida. Risus commodo viverra maecenas accumsan lacus vel facilisis. Lorem ipsum dolor sit amet, consectetur adipiscing elit, sed do eiusmod tempor inc ididunt ut labore et dolore magna aliqua. Quis ipsumsusp endi sse ultrices gravida. Risus commodo viverra maecenas accum san lacus vel facilisis.</p>
  <div class="abs btn" style="left:575px;top:1215px;width:151px;height:50px">Read More</div>
</section>

<section>
  <div class="abs services"></div>
  <h2 class="abs h2 services-title">Our Services</h2>
  <div class="abs svc" style="left:79px;top:1582px"><svg width="100" height="100"><circle cx="50" cy="50" r="48" fill="none" stroke="#fff" stroke-width="3"/><g stroke="#fff" stroke-width="2.5" fill="none"><rect x="30" y="44" width="40" height="28"/><path d="M30 58h40M44 44v14M56 58v14"/></g></svg>Brickwork</div>
  <div class="abs svc" style="left:287px;top:1582px"><svg width="100" height="100"><circle cx="50" cy="50" r="48" fill="none" stroke="#d3dc1d" stroke-width="3"/><g stroke="#d3dc1d" stroke-width="2.5" fill="none"><path d="M34 46a16 16 0 0 1 32 0z"/><rect x="36" y="52" width="28" height="22"/></g></svg>Carpentry</div>
  <div class="abs svc" style="left:494px;top:1582px"><svg width="100" height="100"><circle cx="50" cy="50" r="48" fill="none" stroke="#fff" stroke-width="3"/><g stroke="#fff" stroke-width="2.5" fill="none"><path d="M32 46h36a18 18 0 0 1-36 0zM50 28v18"/><path d="M50 64v12"/></g></svg>Bathroom<br>Fitings</div>
  <div class="abs svc" style="left:702px;top:1582px"><svg width="100" height="100"><circle cx="50" cy="50" r="48" fill="none" stroke="#d3dc1d" stroke-width="3"/><g stroke="#d3dc1d" stroke-width="2.5" fill="none"><rect x="28" y="32" width="44" height="14"/><rect x="28" y="54" width="44" height="20"/><path d="M50 54v20"/></g></svg>Kitchen Fittings</div>
  <div class="abs svc" style="left:910px;top:1582px"><svg width="100" height="100"><circle cx="50" cy="50" r="48" fill="none" stroke="#fff" stroke-width="3"/><g stroke="#fff" stroke-width="2.5" fill="none"><path d="M50 26v36M42 26h16M36 62h28l-6 12H42z"/></g></svg>Groundwork</div>
  <div class="abs svc" style="left:175px;top:1774px"><svg width="100" height="100"><circle cx="50" cy="50" r="48" fill="none" stroke="#d3dc1d" stroke-width="3"/><g stroke="#d3dc1d" stroke-width="2.5" fill="none"><path d="M32 50a18 18 0 0 1 36 0zM28 50h44"/><circle cx="50" cy="64" r="8"/></g></svg>Civil Engineering</div>
  <div class="abs svc" style="left:383px;top:1774px"><svg width="100" height="100"><circle cx="50" cy="50" r="48" fill="none" stroke="#fff" stroke-width="3"/><g stroke="#fff" stroke-width="2.5" fill="none"><path d="M36 66l18-18 10 10-18 18zM58 44l10-10"/></g></svg>Plastering</div>
  <div class="abs svc" style="left:590px;top:1774px"><svg width="100" height="100"><circle cx="50" cy="50" r="48" fill="none" stroke="#d3dc1d" stroke-width="3"/><g stroke="#d3dc1d" stroke-width="2.5" fill="none"><path d="M34 38h20v20h12v14H54a20 20 0 0 1-20-20z"/></g></svg>Plumbing</div>
  <div class="abs svc" style="left:798px;top:1774px"><svg width="100" height="100"><circle cx="50" cy="50" r="48" fill="none" stroke="#fff" stroke-width="3"/><g stroke="#fff" stroke-width="2.5" fill="none"><rect x="32" y="30" width="36" height="14"/><path d="M68 37h4v12H50v8M46 57h8v18h-8z"/></g></svg>Pinting &amp; Decorating</div>
</section>

<section>
  <h2 class="abs h2 projects-title">Our Latest Projects</h2>
  <div class="abs card" style="left:67px;top:2197px;width:519px;height:508px"></div>
  <div class="abs card" style="left:620px;top:2197px;width:519px;height:508px"></div>
  <div class="abs photo" style="left:67px;top:2218px;width:248px;height:452px;background:linear-gradient(180deg,#a9c0d8,#d9d5cc 40%,#4f5a36 75%,#3d4a2a)" role="img" aria-label="Overgrown back garden before clearance"></div>
  <div class="abs tag" style="left:191px;top:2614px">BEFORE</div>
  <div class="abs photo" style="left:334px;top:2280px;width:252px;height:325px;background:linear-gradient(180deg,#cfcfcf,#ececec 45%,#6b5c4c 75%,#5a4b3d)" role="img" aria-label="Cleared back garden after groundwork"></div>
  <div class="abs tag" style="left:474px;top:2550px">AFTER</div>
  <div class="abs photo" style="left:618px;top:2315px;width:250px;height:247px;background:linear-gradient(90deg,#e4e4e4,#f5f5f5 50%,#d6cfc2)" role="img" aria-label="Bathroom before refit"></div>
  <div class="abs tag" style="left:743px;top:2500px">BEFORE</div>
  <div class="abs photo" style="left:885px;top:2250px;width:252px;height:397px;background:linear-gradient(180deg,#eeeeee,#dedede 55%,#555 75%,#222)" role="img" aria-label="Refitted bathroom with glass shower and chequered floor"></div>
  <div class="abs tag" style="left:1026px;top:2550px">AFTER</div>
</section>

<section>
  <div class="abs why"></div>
  <div class="abs photo" style="left:128px;top:2932px;width:392px;height:283px;background:linear-gradient(160deg,#2b3240,#6a6a6a 60%,#c9c0b0)" role="img" aria-label="Finished kitchen with dark units and tiled splashback"></div>
  <div class="abs photo" style="left:318px;top:3037px;width:319px;height:220px;border:3px solid #fff;background:linear-gradient(180deg,#b8c7d6,#8c7a68 50%,#5b4a3c)" role="img" aria-label="New timber decking in rear garden"></div>
  <h2 class="abs h2 why-title">Why Choose Us?</h2>
  <ul class="abs why-list">
    <li><svg width="16" height="16"><circle cx="8" cy="8" r="8" fill="#232e8c"/><path d="M4.5 8l2.5 2.5 4.5-5" stroke="#d3dc1d" stroke-width="2" fill="none"/></svg>Fully Insured</li>
    <li><svg width="16" height="16"><circle cx="8" cy="8" r="8" fill="#232e8c"/><path d="M4.5 8l2.5 2.5 4.5-5" stroke="#d3dc1d" stroke-width="2" fill="none"/></svg>Reliable, Professional Team</li>
    <li><svg width="16" height="16"><circle cx="8" cy="8" r="8" fill="#232e8c"/><path d="M4.5 8l2.5 2.5 4.5-5" stroke="#d3dc1d" stroke-width="2" fill="none"/></svg>High-Quality Finishes</li>
    <li><svg width="16" height="16"><circle cx="8" cy="8" r="8" fill="#232e8c"/><path d="M4.5 8l2.5 2.5 4.5-5" stroke="#d3dc1d" stroke-width="2" fill="none"/></svg>Competitive</li>
    <li><svg width="16" height="16"><circle cx="8" cy="8" r="8" fill="#232e8c"/><path d="M4.5 8l2.5 2.5 4.5-5" stroke="#d3dc1d" stroke-width="2" fill="none"/></svg>Pricing Free quotes</li>
  </ul>
</section>

<section>
  <h2 class="abs h2 testi-title">Testimonials</h2>
  <svg class="abs" style="left:170px;top:3648px" width="26" height="48"><path d="M22 2L4 24l18 22" stroke="#999" stroke-width="3" fill="none"/></svg>
  <svg class="abs" style="left:1003px;top:3648px" width="26" height="48"><path d="M4 2l18 22L4 46" stroke="#999" stroke-width="3" fill="none"/></svg>
  <div class="abs testi-box"></div>
  <p class="abs testi-text">Lorem ipsum dolor sit amet, consectetur adipiscing elit, sed do eiusmod tempor incididunt ut labore et dolore magna aliqua. Quis ipsum suspendisse ultrices gravida. Risus commodo viverra maecenas accumsan lacus vel facilisis.</p>
  <div class="abs quote">&ldquo;</div>
  <div class="abs testi-name">DANIEL MARSH</div>
</section>

<section>
  <div class="abs estimate"></div>
  <div class="abs estimate-text">Free Estimate</div>
  <div class="abs btn" style="left:665px;top:3972px;width:158px;height:48px;font-size:14px">Contact Us</div>
  <div class="abs" style="left:878px;top:3950px;width:130px;height:118px;background:linear-gradient(135deg,#8a8f96,#a0643a)" role="img" aria-label="Claw hammer"></div>
</section>

<footer>
  <div class="abs brand" style="left:122px;top:4148px"><span class="mark"></span>Harwell Builds</div>
  <div class="abs foot-h" style="left:407px;top:4130px">Links</div>
  <ul class="abs foot-list" style="left:407px;top:4172px"><li>Privacy Policy</li><li>Terms Of Use</li><li>Sitemap</li></ul>
  <div class="abs foot-h" style="left:602px;top:4130px">Menu</div>
  <ul class="abs foot-list" style="left:602px;top:4172px"><li>Home</li><li>About Us</li><li>Services</li><li>Gallery</li><li>Contact</li></ul>
  <div class="abs foot-h" style="left:783px;top:4130px">Contact</div>
  <div class="abs contact-row" style="left:783px;top:4173px"><span class="ico"><svg width="12" height="9" viewBox="0 0 24 18"><rect width="24" height="18" fill="#fff"/><path d="M2 2l10 8 10-8" stroke="#232e8c" stroke-width="2.5" fill="none"/></svg></span>hello@harwellbuilds.co.uk</div>
  <div class="abs contact-row" style="left:783px;top:4205px"><span class="ico"><svg width="12" height="12" viewBox="0 0 24 24"><path fill="#fff" d="M6.6 10.8a15 15 0 0 0 6.6 6.6l2.2-2.2c.3-.3.7-.4 1-.2 1.1.4 2.3.6 3.6.6.6 0 1 .4 1 1V20c0 .6-.4 1-1 1A17 17 0 0 1 3 4c0-.6.4-1 1-1h3.5c.6 0 1 .4 1 1 0 1.3.2 2.5.6 3.6.1.3 0 .7-.2 1z"/></svg></span>0790 000 1234</div>
  <div class="abs contact-row" style="left:783px;top:4240px"><span class="ico"><svg width="10" height="14" viewBox="0 0 20 28"><path fill="#fff" d="M10 0a10 10 0 0 1 10 10c0 7-10 18-10 18S0 17 0 10A10 10 0 0 1 10 0z"/><circle cx="10" cy="10" r="4" fill="#232e8c"/></svg></span>12 Example Road, 2nd Floor<br>Lorem Ipsum, AB 10001</div>
  <div class="abs rule"></div>
  <p class="abs copy">© 2025 Harwell Builds. All Rights Reserved.</p>
</footer>

</body>
</html>
```